Designa business card please "AQUAVANT"

i need business cards designed for my plumbing business, i need them to be modern and eye catching. something unique and different. please take your time on a good design and be diffrent, dont copy what you see online. i wouldnt mind big logo on the front and maybe details at the back. hit me with what you have.

i will attach my business logo please use that. thanks

```html
<!DOCTYPE html>
<html lang="en">
<head>
<meta charset="utf-8">
<title>AQUAVANT Business Card</title>
<link href="https://fonts.googleapis.com/css2?family=Montserrat:wght@500;600;700&family=Open+Sans:wght@400&display=swap" rel="stylesheet">
<style>
  :root {
    --backdrop: #4d4d4d;
    --card: #ffffff;
    --brand-blue: #0f57a6;
    --brand-gray: #858585;
    --text-gray: #6e6e6e;
    --contact-gray: #555555;
  }
  * { margin: 0; padding: 0; box-sizing: border-box; }
  html, body {
    width: 1200px; height: 1176px; overflow: hidden;
    background: var(--backdrop);
  }
  .canvas { position: relative; width: 1200px; height: 1176px; }
  .card {
    position: absolute; left: 209px; width: 782px; height: 446px;
    background: var(--card); border-radius: 22px; overflow: hidden;
  }
  .card--front { top: 91px; }
  .card--back { top: 641px; }
  .card__band { position: absolute; left: 0; bottom: 0; width: 782px; height: 27px; display: block; }
  .person { position: absolute; left: 60px; top: 110px; }
  .person__name {
    font-family: "Montserrat", sans-serif; font-weight: 700;
    font-size: 29px; letter-spacing: 0.3px; color: var(--text-gray); line-height: 1;
  }
  .person__role {
    margin-top: 8px; font-family: "Open Sans", sans-serif; font-size: 17px;
    color: var(--text-gray); line-height: 1;
  }
  .person__rule {
    position: absolute; left: 60px; top: 181px; width: 284px; height: 2px;
    background: linear-gradient(90deg, rgba(15,87,166,0.15), var(--brand-blue));
  }
  .contacts { position: absolute; left: 60px; top: 258px; list-style: none; }
  .contacts__item {
    display: flex; align-items: center; gap: 10px; height: 26px;
    font-family: "Open Sans", sans-serif; font-size: 19px; color: var(--contact-gray);
  }
  .contacts__icon { width: 14px; height: 14px; flex: none; }
  .brand {
    position: absolute; display: flex; align-items: center; gap: 10px;
    font-family: "Montserrat", sans-serif; font-weight: 700; font-size: 38px;
    color: var(--brand-blue); letter-spacing: 0.5px; line-height: 1;
  }
  .brand__square { width: 16px; height: 16px; background: var(--brand-blue); flex: none; }
  .card--front .brand { left: 462px; top: 230px; }
  .card--back .brand { left: 50%; top: 236px; transform: translateX(-50%); }
</style>
</head>
<body>
<main class="canvas">
  <section class="card card--front" aria-label="Card front">
    <div class="person">
      <p class="person__name">MARA KELLVEN</p>
      <p class="person__role">Speaker, Writer, Creator</p>
    </div>
    <div class="person__rule"></div>
    <ul class="contacts">
      <li class="contacts__item">
        <svg class="contacts__icon" viewBox="0 0 14 14"><path fill="var(--brand-blue)" d="M1 5c0-2 2-3 6-3s6 1 6 3v1h-3V5H4v1H1zM3 7h8l1 5H2z"/></svg>
        +1(555) 0123456
      </li>
      <li class="contacts__item">
        <svg class="contacts__icon" viewBox="0 0 14 14"><rect x="1" y="3" width="12" height="8" fill="var(--brand-blue)"/><path d="M1 3l6 5 6-5" fill="none" stroke="#fff" stroke-width="1.2"/></svg>
        mara@kellven.com
      </li>
      <li class="contacts__item">
        <svg class="contacts__icon" viewBox="0 0 14 14"><circle cx="7" cy="7" r="6" fill="var(--brand-blue)"/><path d="M1 7h12M7 1c-3 3-3 9 0 12M7 1c3 3 3 9 0 12" fill="none" stroke="#fff" stroke-width="0.9"/></svg>
        www.kellven.com
      </li>
    </ul>
    <div class="brand"><span class="brand__square"></span>AQUAVANT</div>
    <svg class="card__band" viewBox="0 0 782 27" preserveAspectRatio="none">
      <polygon points="0,0 436,0 450,27 0,27" fill="var(--brand-blue)"/>
      <polygon points="444,0 782,0 782,27 458,27" fill="var(--brand-gray)"/>
    </svg>
  </section>

  <section class="card card--back" aria-label="Card back">
    <div class="brand"><span class="brand__square"></span>AQUAVANT</div>
    <svg class="card__band" viewBox="0 0 782 27" preserveAspectRatio="none">
      <polygon points="0,0 436,0 450,27 0,27" fill="var(--brand-blue)"/>
      <polygon points="444,0 782,0 782,27 458,27" fill="var(--brand-gray)"/>
    </svg>
  </section>
</main>
</body>
</html>
```